fix and make current flyer more professorial looking

we have the attached flyer that we want to be reworked. Feel free to completely redo it but we do like the main image about where it is. here are some other thoughts.

Too much space for Korvo Logo
Real Competitive should be a different color
Bullets I want in their own callout section, better than it is there now
Logos should be closer to the bottom in a line and not at big

Highlight speed cost and support

```html
<!DOCTYPE html>
<html lang="en">
<head>
<meta charset="utf-8">
<title>Korvo Distributing – Flyer Series</title>
<link rel="stylesheet" href="https://fonts.googleapis.com/css2?family=Roboto:wght@300;400;500;700;900&display=swap">
<style>
:root{
  --page:#efefef;
  --paper:#ffffff;
  --ink:#111418;
  --slate:#6f8aa6;
  --slate-light:#7f98b2;
  --slate-dark:#5f7793;
  --slate-deep:#687f98;
  --navy:#1b2733;
  --white:#ffffff;
  --i-blue:#1e8fe0;
  --i-pink:#e0218a;
  --i-orange:#f26a2a;
  --i-green:#7ac143;
  --i-red:#d3302f;
  --i-power:#1e6fd9;
  --i-teal:#1aa39a;
  --i-tan:#b59a7a;
  --i-amber:#f3a533;
}
*{box-sizing:border-box;margin:0;padding:0}
html,body{width:1200px;height:1200px;overflow:hidden;background:var(--page);font-family:"Roboto",Arial,sans-serif;color:var(--ink)}
.flyer{position:absolute;width:441px;height:566px;background:var(--paper);box-shadow:0 4px 10px rgba(0,0,0,.35);overflow:hidden}
.flyer--products{left:124px;top:36px}
.flyer--services{left:620px;top:36px}
.flyer--media{left:380px;top:620px}
.flyer svg.art{position:absolute;left:0;top:0}
.abs{position:absolute}
.brand{left:0;width:100%;text-align:center;font-weight:700;font-size:44px;letter-spacing:3px;color:var(--ink);line-height:1}
.rule{height:1px;background:#222;left:120px;width:201px}
.tagline{left:0;width:100%;text-align:center;font-weight:700;font-size:9.6px;line-height:13px;text-transform:uppercase;color:var(--ink)}
.pill{left:142px;top:288px;width:156px;height:21px;background:var(--slate);color:var(--white);border-radius:8px;text-align:center;font-weight:700;font-size:14px;line-height:21px;letter-spacing:.3px}
.card{position:absolute;width:70px}
.card__head{height:21px;background:var(--navy);color:var(--white);font-weight:700;font-size:6.4px;text-align:center;padding-top:11px;border-radius:2px 2px 0 0;white-space:nowrap}
.card__body{height:38px;background:var(--slate);border-radius:0 0 3px 3px;color:#eef2f6;font-size:4.6px;line-height:6.8px;padding:5px 6px;display:flex;gap:6px;overflow:hidden}
.card__body ul{list-style:none;flex:none}
.card__body li{white-space:nowrap}
.card__body li::before{content:"• "}
.card__icon{position:absolute;left:25px;top:-10px;width:20px;height:20px;border-radius:50%;border:1.5px solid #fff;display:flex;align-items:center;justify-content:center}
.card__icon i{display:block;width:7px;height:7px;background:#fff;border-radius:1px}
.blurb{left:0;width:100%;text-align:center;font-size:6.2px;line-height:9.5px;color:#e6ecf2;font-weight:300}
.blurb b{font-weight:700;color:#fff}
.contact{left:0;width:100%;display:flex;justify-content:center;align-items:center;gap:10px;color:var(--white);font-weight:700;font-size:8px}
.contact span{display:flex;align-items:center;gap:5px}
.contact .sep{width:1px;height:10px;background:#fff}
.footer-band{left:0;width:100%;background:var(--slate-dark)}
.col-title{color:var(--white);font-weight:700;font-size:14.5px;line-height:13px}
.col-title small{display:block;font-weight:400;font-size:14.5px}
.svc{list-style:none;color:var(--white);font-weight:700;font-size:7.4px;line-height:13.25px}
.svc li::before{content:"• "}
.note{left:0;width:100%;text-align:center;font-size:5.6px;line-height:9.5px;font-weight:700;color:var(--ink)}
.callout{background:var(--white);border:3px solid var(--slate);font-size:7.3px;line-height:9.6px;color:var(--ink);padding:3px 7px;overflow:hidden}
.apps{background:var(--white);border:2.5px solid var(--slate);padding:4px 8px;font-size:5.2px;line-height:6.6px}
.apps ul{list-style:none;font-style:italic;font-weight:700;margin-left:4px}
.apps li::before{content:"• "}
.partners{left:90px;top:438px;width:262px;display:flex;align-items:center;justify-content:space-between}
.partners span{font-weight:700;font-size:13px;color:var(--navy)}
</style>
</head>
<body>

<section class="flyer flyer--products">
  <svg class="art" width="441" height="566" viewBox="0 0 441 566">
    <defs>
      <linearGradient id="chip" x1="0" y1="0" x2="1" y2="1"><stop offset="0" stop-color="#0a1a33"/><stop offset=".5" stop-color="#2a63b0"/><stop offset="1" stop-color="#081428"/></linearGradient>
      <linearGradient id="board" x1="0" y1="0" x2="0" y2="1"><stop offset="0" stop-color="#3f6a6a"/><stop offset="1" stop-color="#1c2c38"/></linearGradient>
      <linearGradient id="ram" x1="0" y1="0" x2="1" y2="1"><stop offset="0" stop-color="#b9c4cc"/><stop offset="1" stop-color="#2b3d52"/></linearGradient>
    </defs>
    <polygon points="0,60 96,90 96,241 0,228" fill="url(#board)" role="img" aria-label="Photo of server memory modules"/>
    <polygon points="98,91 220,128 344,92 344,241 220,258 98,241" fill="url(#chip)" role="img" aria-label="Photo of a glowing processor on a circuit board"/>
    <polygon points="348,90 441,64 441,234 348,244" fill="url(#ram)" role="img" aria-label="Photo of memory chips on a circuit board"/>
    <rect x="0" y="296" width="441" height="3" fill="var(--slate)"/>
    <polygon points="0,442 220,508 441,442 441,566 0,566" fill="var(--slate)"/>
  </svg>

  <div class="abs brand" style="top:16px">KORVO</div>
  <div class="abs rule" style="top:66px"></div>
  <div class="abs tagline" style="top:78px">Full service, stocking distributor<br>of top-tier data center products</div>
  <div class="abs pill">PRODUCT OFFERING</div>

  <div class="card" style="left:22px;top:324px"><div class="card__icon" style="background:var(--i-blue)"><i></i></div><div class="card__head">SERVERS</div><div class="card__body"><ul><li>Arvex Prolane</li><li>Nexar X-Series</li><li>Delmont Edge</li></ul></div></div>
  <div class="card" style="left:104px;top:324px"><div class="card__icon" style="background:var(--i-pink)"><i></i></div><div class="card__head">NETWORKING</div><div class="card__body"><ul><li>Orbita</li><li>Cirrox</li><li>Junova</li></ul><ul><li>Bramble</li><li>Nortrax</li></ul></div></div>
  <div class="card" style="left:185px;top:324px"><div class="card__icon" style="background:var(--i-orange)"><i></i></div><div class="card__head">STORAGE</div><div class="card__body" style="flex-wrap:wrap;gap:0 6px"><ul><li>Netvale</li><li>Qlinq</li></ul><ul><li>Hikaro</li><li>Emvera</li></ul><ul><li>Arvex Storeworks</li></ul></div></div>
  <div class="card" style="left:267px;top:324px"><div class="card__icon" style="background:var(--i-green)"><i></i></div><div class="card__head">MEMORY</div><div class="card__body" style="gap:5px"><ul><li>Arvex</li><li>Cirrox</li><li>Nexar</li></ul><ul><li>Approved<br>&nbsp;&nbsp;Memory</li></ul></div></div>
  <div class="card" style="left:350px;top:324px"><div class="card__icon" style="background:var(--i-red)"><i></i></div><div class="card__head">VIRTUALIZATION</div><div class="card__body" style="padding-left:22px"><ul><li>Vmarq</li><li>Veyra</li></ul></div></div>

  <div class="card" style="left:62px;top:397px"><div class="card__icon" style="background:var(--i-power)"><i></i></div><div class="card__head">POWER</div><div class="card__body" style="height:39px"><ul><li>Apexa</li><li>Triplex</li></ul></div></div>
  <div class="card" style="left:145px;top:397px"><div class="card__icon" style="background:var(--i-teal)"><i></i></div><div class="card__head">SECURITY</div><div class="card__body" style="height:39px;padding-left:18px"><ul><li>Sonvault</li><li>Junova</li><li>Wardline</li></ul></div></div>
  <div class="card" style="left:226px;top:397px"><div class="card__icon" style="background:var(--i-tan)"><i></i></div><div class="card__head">DISK STORAGE</div><div class="card__body" style="height:39px;padding-left:14px;padding-top:3px"><ul><li>Seabrook</li><li>Westdrive</li><li>Samvio</li><li>Hgora</li></ul></div></div>
  <div class="card" style="left:308px;top:397px"><div class="card__icon" style="background:var(--i-amber)"><i></i></div><div class="card__head">TELEPHONY</div><div class="card__body" style="height:39px;font-size:5.4px;padding-top:8px"><ul><li>Avalo</li><li>Cirrox</li></ul><ul><li>Nortrax</li><li>Polyra</li></ul></div></div>

  <p class="abs blurb" style="top:516px">With over 50 years of combined expertise in the sourcing, configuring, and delivering of customized business solutions,<br><b>Korvo Distributing</b> is committed to providing its partners with impactful, timely alternatives that drive profit to the bottom line</p>
  <div class="abs footer-band" style="top:538px;height:20px"></div>
  <div class="abs contact" style="top:542px">
    <span><svg width="9" height="9" viewBox="0 0 10 10"><path d="M2 1l2 2-1 1.5c.6 1.2 1.4 2 2.5 2.5L7 6l2 2-1.3 1.5C4.5 9 1 5.5.5 2.3z" fill="#fff"/></svg>(555) 014-2290</span><i class="sep"></i>
    <span><svg width="10" height="8" viewBox="0 0 10 8"><rect x=".5" y=".5" width="9" height="7" fill="none" stroke="#fff"/><path d="M.5 .5l4.5 4 4.5-4" fill="none" stroke="#fff"/></svg>info@korvodistributing.com</span><i class="sep"></i>
    <span><svg width="9" height="9" viewBox="0 0 10 10"><circle cx="5" cy="5" r="4.3" fill="none" stroke="#fff" stroke-width="1.2"/><path d="M.7 5h8.6M5 .7c2.2 2.5 2.2 6.1 0 8.6M5 .7c-2.2 2.5-2.2 6.1 0 8.6" fill="none" stroke="#fff" stroke-width=".8"/></svg>www.korvodistributing.com</span>
  </div>
</section>

<section class="flyer flyer--services">
  <svg class="art" width="441" height="566" viewBox="0 0 441 566">
    <defs>
      <linearGradient id="lab" x1="0" y1="0" x2="0" y2="1"><stop offset="0" stop-color="#9fb2c2"/><stop offset=".55" stop-color="#4d6f93"/><stop offset="1" stop-color="#c9cfd3"/></linearGradient>
      <linearGradient id="warehouse" x1="0" y1="0" x2="0" y2="1"><stop offset="0" stop-color="#b7c2cc"/><stop offset=".6" stop-color="#c9a27a"/><stop offset="1" stop-color="#dcdcdc"/></linearGradient>
    </defs>
    <polygon points="0,68 219,128 219,252 0,252" fill="url(#lab)" role="img" aria-label="Photo of a configuration lab with blue workbenches"/>
    <polygon points="221,127 441,68 441,252 221,252" fill="url(#warehouse)" role="img" aria-label="Photo of a warehouse with boxes on a roller conveyor"/>
    <rect x="0" y="252" width="220" height="37" fill="var(--slate-light)"/>
    <rect x="220" y="252" width="221" height="37" fill="var(--slate)"/>
    <rect x="0" y="289" width="441" height="3" fill="#fff"/>
    <rect x="0" y="292" width="220" height="178" fill="var(--slate-light)"/>
    <rect x="220" y="292" width="221" height="178" fill="var(--slate-deep)"/>
    <polygon points="0,479 220,541 441,479 441,566 0,566" fill="var(--slate)"/>
  </svg>

  <div class="abs brand" style="top:20px">KORVO</div>
  <div class="abs rule" style="top:70px"></div>
  <div class="abs tagline" style="top:76px;font-size:9.2px;line-height:11.5px">Expert engineering support from solution design,<br>to implementation, to post-sales support</div>

  <div class="abs col-title" style="left:58px;top:264px">SERVICES</div>
  <div class="abs col-title" style="left:277px;top:258px">PROFESSIONAL<small>SERVICES</small></div>

  <ul class="abs svc" style="left:58px;top:295px">
    <li>Integration And Configuration</li><li>Pre And Post-Sales Support</li><li>Same Day Shipping</li><li>Finance And Flooring Options</li><li>Blind Drop Shipping</li><li>Plug And Play Solutions</li><li>OS Loading</li><li>Vmarq Environment Testing</li><li>Installations</li><li>Decommissioning</li><li>Data Migration</li><li>Data Center Migration</li><li>Data Center Relocation</li>
  </ul>
  <ul class="abs svc" style="left:277px;top:295px">
    <li>Installations</li><li>Data Center Migration</li><li>Data Center Relocation</li><li>Data Migration</li><li>Decommissioning</li><li>Flexible Warranty Options</li><li>Post Warranty Options</li><li>OEM Warranties</li><li>IMACD Services (Installations,<br>&nbsp;&nbsp;Move, Add, Change, Disposal)</li>
  </ul>

  <p class="abs note" style="top:478px">Usher your customers through the confusing IT development and deployment process to improve<br>your close ratio on larger, more profitable deals and increase lifetime customer value</p>

  <div class="abs contact" style="top:540px">
    <span><svg width="9" height="9" viewBox="0 0 10 10"><path d="M2 1l2 2-1 1.5c.6 1.2 1.4 2 2.5 2.5L7 6l2 2-1.3 1.5C4.5 9 1 5.5.5 2.3z" fill="#fff"/></svg>(555) 014-2290</span><i class="sep"></i>
    <span><svg width="10" height="8" viewBox="0 0 10 8"><rect x=".5" y=".5" width="9" height="7" fill="none" stroke="#fff"/><path d="M.5 .5l4.5 4 4.5-4" fill="none" stroke="#fff"/></svg>info@korvodistributing.com</span><i class="sep"></i>
    <span><svg width="9" height="9" viewBox="0 0 10 10"><circle cx="5" cy="5" r="4.3" fill="none" stroke="#fff" stroke-width="1.2"/><path d="M.7 5h8.6M5 .7c2.2 2.5 2.2 6.1 0 8.6M5 .7c-2.2 2.5-2.2 6.1 0 8.6" fill="none" stroke="#fff" stroke-width=".8"/></svg>www.korvodistributing.com</span>
  </div>
</section>

<section class="flyer flyer--media">
  <svg class="art" width="441" height="566" viewBox="0 0 441 566">
    <defs>
      <linearGradient id="control" x1="0" y1="0" x2="0" y2="1"><stop offset="0" stop-color="#0d1420"/><stop offset=".45" stop-color="#27496e"/><stop offset="1" stop-color="#05080d"/></linearGradient>
    </defs>
    <polygon points="0,66 0,262 441,262 441,66 220,132" fill="url(#control)" role="img" aria-label="Photo of a broadcast control room with walls of monitors"/>
    <polygon points="0,0 441,0 441,66 220,132 0,66" fill="#fff"/>
    <rect x="0" y="262" width="441" height="8" fill="var(--slate)"/>
    <polygon points="0,444 220,508 441,444 441,566 0,566" fill="var(--slate)"/>
    <rect x="0" y="539" width="441" height="20" fill="var(--slate-dark)"/>
  </svg>

  <div class="abs brand" style="top:16px">KORVO</div>
  <div class="abs rule" style="top:72px"></div>
  <div class="abs tagline" style="top:80px;font-size:9.8px;line-height:12.5px">Real competitive advantages<br>in media and entertainment</div>

  <div class="abs callout" style="left:14px;top:278px;width:196px;height:72px;text-align:center">When it comes to competitive advantages, it doesn't get much better than being able to cut delivery time by 80%, decrease cost by up to 30% from traditional distribution outlets, and provide a plug-and play solution with a variety of different manufacturer's components.</div>
  <div class="abs callout" style="left:230px;top:278px;width:196px;height:72px;padding-left:9px">KORVO has spent the last 10 years navigating the media and entertainment landscape to be able to provide you with the most current, reliable platform to optimize the user experience.</div>

  <div class="abs apps" style="left:118px;top:356px;width:200px;height:80px">
    Our digital media platforms are ideal for the following types of applications
    <ul><li>Media Retention</li><li>Video Transport</li><li>Video Content Management</li><li>Video Encoding / Decoding</li><li>Video Stream Recording</li><li>On-Demand Media</li><li>Digital Archive &amp; Retrieval</li><li>Collaborative Video Conferencing</li><li>Webcasting</li></ul>
  </div>

  <div class="abs partners"><span>Sportline</span><span>Bellwave Media</span><span>Tunevue</span><span>Abcora</span></div>

  <p class="abs blurb" style="top:517px">With over 50 years of combined expertise in the sourcing, configuring, and delivering of customized business solutions.<br><b>Korvo Distributing</b> is committed to providing its partners with impactful, timely alternatives that drive profit to the bottom line</p>
  <div class="abs contact" style="top:543px">
    <span><svg width="9" height="9" viewBox="0 0 10 10"><path d="M2 1l2 2-1 1.5c.6 1.2 1.4 2 2.5 2.5L7 6l2 2-1.3 1.5C4.5 9 1 5.5.5 2.3z" fill="#fff"/></svg>(555) 014-2290</span><i class="sep"></i>
    <span><svg width="10" height="8" viewBox="0 0 10 8"><rect x=".5" y=".5" width="9" height="7" fill="none" stroke="#fff"/><path d="M.5 .5l4.5 4 4.5-4" fill="none" stroke="#fff"/></svg>info@korvodistributing.com</span><i class="sep"></i>
    <span><svg width="9" height="9" viewBox="0 0 10 10"><circle cx="5" cy="5" r="4.3" fill="none" stroke="#fff" stroke-width="1.2"/><path d="M.7 5h8.6M5 .7c2.2 2.5 2.2 6.1 0 8.6M5 .7c-2.2 2.5-2.2 6.1 0 8.6" fill="none" stroke="#fff" stroke-width=".8"/></svg>www.korvodistributing.com</span>
  </div>
</section>

</body>
</html>
```